Gilt Corner Shop Sign

Name of company
Gilt Corner
Gilt Corner is a picture framing shop and art gallery selling custom frames, art work and gifts.
Needing a design for shop front sign.

The Sign
The sign is above the shop front window and is approximately 12 feet wide by 43 inches high. White on black. White striped boarder that looks like a picture frame with Gilt Corner in classic lettering including space for a phone number and it may or may not need to include description of services. Something cute in one area like a picture frame with a heart inside. A friendly feel like something that would be special and feels like yours. I have attached a photo of the existing sign to be replaced.

Thank you for your time.

```html
<!DOCTYPE html>
<html lang="en">
<head>
<meta charset="utf-8">
<title>Gilt Corner Shop Sign</title>
<link rel="stylesheet" href="https://fonts.googleapis.com/css2?family=Antonio:wght@400&family=Open+Sans:wght@400&display=swap">
<style>
  :root {
    --backdrop: #8c8c8c;
    --sign-black: #050505;
    --sign-white: #ffffff;
    --heart-red: #e01a47;
  }
  * { margin: 0; padding: 0; box-sizing: border-box; }
  html, body {
    width: 1200px;
    height: 1200px;
    overflow: hidden;
    background: var(--backdrop);
  }
  .canvas {
    position: relative;
    width: 1200px;
    height: 1200px;
  }
  .shop-sign {
    position: absolute;
    left: 103px;
    top: 450px;
    width: 994px;
    height: 300px;
    background: repeating-linear-gradient(
      -45deg,
      var(--sign-white) 0 9px,
      var(--sign-black) 9px 18px
    );
  }
  .sign-panel {
    position: absolute;
    inset: 21px 21px 21px 22px;
    background: var(--sign-black);
  }
  .brand-square {
    position: absolute;
    left: 90px;
    top: 95px;
    width: 66px;
    height: 66px;
    background: var(--heart-red);
  }
  .sign-title {
    position: absolute;
    left: 232px;
    top: 38px;
    width: 680px;
    font-family: "Antonio", "Arial Narrow", sans-serif;
    font-weight: 400;
    font-size: 126px;
    line-height: 1;
    letter-spacing: 6px;
    color: var(--sign-white);
    white-space: nowrap;
    text-transform: uppercase;
  }
  .sign-services {
    position: absolute;
    left: 232px;
    top: 170px;
    width: 680px;
    font-family: "Open Sans", Arial, sans-serif;
    font-weight: 400;
    font-size: 21.5px;
    line-height: 30px;
    letter-spacing: 0.8px;
    color: var(--sign-white);
    text-align: center;
    text-transform: uppercase;
  }
</style>
</head>
<body>
  <main class="canvas">
    <div class="shop-sign">
      <div class="sign-panel">
        <div class="brand-square"></div>
        <h1 class="sign-title">Gilt Corner</h1>
        <p class="sign-services">Picture framing shop and art gallery<br>selling custom frames, art work and gifts.</p>
      </div>
    </div>
  </main>
</body>
</html>
```